Need business cards for our e-assessment business

We need professional looking business cards for our e-assessment business based in Europe. Our company is called Velmora.

You can just use sample name and addresses.

The colours we use are:

#70abe4 (blue)
#FF6600 (orange)

The back side should say: E-testing made simple

This is the print-shop we are using. Please look at the link for info about formats: http://nl.pribbly-print.com/help/faq/using-my-own-artwork.html

Target Market(s)

Target market is education and large corporations

Industry/Entity Type

Business

```html
<!DOCTYPE html>
<html lang="en">
<head>
<meta charset="utf-8">
<title>Velmora business cards</title>
<link rel="stylesheet" href="https://fonts.googleapis.com/css2?family=Arimo:wght@400;700&family=Open+Sans:ital,wght@1,400&display=swap">
<style>
  :root {
    --backdrop: #2e2f33;
    --card: #ffffff;
    --orange: #e8641a;
    --peach: #fdd9c4;
    --ink: #111111;
    --wordmark: #2f2c2a;
  }
  html, body {
    margin: 0;
    width: 1200px;
    height: 821px;
    overflow: hidden;
    background: var(--backdrop);
  }
  .canvas {
    position: relative;
    width: 1200px;
    height: 821px;
  }
  .card {
    position: absolute;
    left: 280px;
    width: 640px;
    height: 366px;
    background: var(--card);
    overflow: hidden;
  }
  .card--back { top: 30px; }
  .card--front { top: 425px; }

  /* Back side */
  .back-circle {
    position: absolute;
    left: 400px;
    top: 55px;
    width: 260px;
    height: 260px;
    border-radius: 50%;
    background: var(--peach);
  }
  .tagline {
    position: absolute;
    left: 80px;
    top: 112px;
    margin: 0;
    font-family: "Open Sans", sans-serif;
    font-style: italic;
    font-weight: 400;
    font-size: 46px;
    line-height: 1.2;
    color: var(--ink);
    white-space: nowrap;
  }

  /* Front side */
  .accent-bar {
    position: absolute;
    left: 588px;
    width: 11px;
    background: var(--orange);
  }
  .accent-bar--top { top: 0; height: 22px; }
  .accent-bar--main { top: 112px; bottom: 0; }
  .brand {
    position: absolute;
    right: 28px;
    top: 24px;
    display: flex;
    align-items: center;
    gap: 16px;
  }
  .brand-dot {
    width: 74px;
    height: 74px;
    border-radius: 50%;
    background: var(--orange);
  }
  .brand-name {
    font-family: "Arimo", sans-serif;
    font-weight: 400;
    font-size: 58px;
    line-height: 1;
    color: var(--wordmark);
    letter-spacing: -1px;
  }
  .person {
    position: absolute;
    left: 40px;
    top: 132px;
    font-family: "Arimo", sans-serif;
  }
  .person-name {
    margin: 0;
    font-size: 24px;
    font-weight: 400;
    color: var(--ink);
    line-height: 1.1;
  }
  .person-name .surname { color: var(--orange); font-weight: 700; }
  .person-role {
    margin: 2px 0 0;
    font-size: 21px;
    font-weight: 700;
    color: var(--orange);
  }
  .contact {
    list-style: none;
    margin: 22px 0 0;
    padding: 0;
    font-size: 15px;
    color: var(--ink);
  }
  .contact li {
    display: flex;
    align-items: center;
    gap: 6px;
    margin-bottom: 9px;
  }
  .contact .phone { font-size: 17px; }
  .contact .address { font-size: 13px; }
  .contact svg { flex: none; }
</style>
</head>
<body>
<main class="canvas">
  <section class="card card--back" aria-label="Back of card">
    <div class="back-circle"></div>
    <p class="tagline">E-testing made simple</p>
  </section>

  <section class="card card--front" aria-label="Front of card">
    <div class="accent-bar accent-bar--top"></div>
    <div class="accent-bar accent-bar--main"></div>
    <div class="brand">
      <div class="brand-dot"></div>
      <span class="brand-name">velmora</span>
    </div>
    <div class="person">
      <h1 class="person-name">ANNA <span class="surname">VERHOEF</span></h1>
      <p class="person-role">CEO</p>
      <ul class="contact">
        <li class="phone">
          <svg width="20" height="20" viewBox="0 0 20 20" aria-hidden="true"><circle cx="10" cy="10" r="9" fill="none" stroke="#111" stroke-width="1.3"/><path d="M6.5 5.5l2 0 1 2.5-1.3 1c.6 1.3 1.5 2.2 2.8 2.8l1-1.3 2.5 1v2c-4.5.3-8.3-3.5-8-8z" fill="#111"/></svg>
          +31-20-5550147
        </li>
        <li class="address">
          <svg width="20" height="20" viewBox="0 0 20 20" aria-hidden="true"><circle cx="10" cy="10" r="9" fill="none" stroke="#111" stroke-width="1.3"/><path d="M4.5 10.5L10 5l5.5 5.5h-1.7V15h-2.6v-3H8.8v3H6.2v-4.5z" fill="#111"/></svg>
          14 KEIZERSWEG, UNIT 3, NL -1017AB
        </li>
        <li class="email">
          <svg width="20" height="20" viewBox="0 0 20 20" aria-hidden="true"><circle cx="10" cy="10" r="9" fill="none" stroke="#111" stroke-width="1.3"/><rect x="5" y="6.5" width="10" height="7" fill="none" stroke="#111" stroke-width="1.2"/><path d="M5 6.5l5 4 5-4" fill="none" stroke="#111" stroke-width="1.2"/></svg>
          annaverhoef@velmora.com
        </li>
      </ul>
    </div>
  </section>
</main>
</body>
</html>
```